Kestrel Aid Services Banner Ad

Need a 750 x 250-pixel banner ad with the company Logo included. Please see company website at www.kestrelaidservices.com for more information.

```html
<!DOCTYPE html>
<html lang="en">
<head>
<meta charset="utf-8">
<title>Kestrel Aid Services – Banner Ads 750 x 250</title>
<link href="https://fonts.googleapis.com/css2?family=Roboto:wght@400;500;700&display=swap" rel="stylesheet">
<style>
  :root {
    --brand-blue: #0f5a8c;
    --brand-blue-dark: #0a4670;
    --brand-blue-light: #2a86c2;
    --brand-green: #7dc242;
    --brand-green-light: #b5e061;
    --brand-green-dark: #4c9f16;
    --ink: #2b2b2b;
    --paper: #ffffff;
    --pattern: #eef2f6;
    --photo-warm-a: #c46a4a;
    --photo-warm-b: #6f8f4a;
    --photo-green-a: #7f9b5a;
    --photo-green-b: #d9c6a8;
  }
  html, body {
    margin: 0;
    padding: 0;
    width: 1200px;
    height: 1044px;
    overflow: hidden;
    background: var(--paper);
    font-family: "Roboto", Arial, sans-serif;
  }
  .board {
    position: relative;
    width: 1200px;
    height: 1044px;
  }
  .board-backdrop {
    position: absolute;
    inset: 0;
  }
  .board-title {
    position: absolute;
    top: 78px;
    left: 0;
    width: 1194px;
    margin: 0;
    text-align: center;
    font-size: 50px;
    font-weight: 700;
    color: var(--brand-blue);
    letter-spacing: 0.5px;
  }
  .banner {
    position: absolute;
    left: 109px;
    width: 974px;
    height: 325px;
    box-shadow: 0 4px 18px rgba(0,0,0,0.18);
    background: var(--paper);
  }
  .banner--arc { top: 188px; }
  .banner--curve { top: 605px; }
  .banner svg { display: block; width: 974px; height: 325px; }
  .brand-name { font-family: "Roboto", Arial, sans-serif; font-weight: 700; fill: var(--brand-blue); font-size: 14px; }
  .headline { font-family: "Roboto", Arial, sans-serif; font-weight: 700; font-size: 16.5px; }
  .headline--light { fill: var(--paper); }
  .headline--dark { fill: var(--brand-blue); }
  .feature-text { font-family: "Roboto", Arial, sans-serif; font-size: 11.5px; }
  .feature-text--light { fill: var(--paper); font-weight: 500; }
  .feature-text--dark { fill: var(--ink); font-weight: 400; }
  .feature-badge { fill: var(--brand-green); stroke: var(--paper); stroke-width: 3; }
</style>
</head>
<body>
<main class="board">
  <svg class="board-backdrop" width="1200" height="1044" viewBox="0 0 1200 1044" aria-hidden="true">
    <defs>
      <linearGradient id="backdropGreen" x1="1" y1="0" x2="0.4" y2="1">
        <stop offset="0" stop-color="var(--brand-green-light)"/>
        <stop offset="1" stop-color="var(--brand-green-dark)"/>
      </linearGradient>
    </defs>
    <polygon points="1200,32 1200,1044 0,1044 0,1026" fill="url(#backdropGreen)"/>
  </svg>

  <h1 class="board-title">750 x 250</h1>

  <!-- Banner variant A: arc layout -->
  <section class="banner banner--arc" aria-label="Kestrel Aid Services banner, arc layout">
    <svg viewBox="0 0 750 250">
      <defs>
        <radialGradient id="orbA" cx="0.4" cy="0.35" r="0.7">
          <stop offset="0" stop-color="var(--brand-blue-light)"/>
          <stop offset="1" stop-color="var(--brand-blue-dark)"/>
        </radialGradient>
        <linearGradient id="photoA" x1="0" y1="0" x2="1" y2="1">
          <stop offset="0" stop-color="var(--photo-warm-b)"/>
          <stop offset="0.5" stop-color="#d89a78"/>
          <stop offset="1" stop-color="var(--photo-warm-a)"/>
        </linearGradient>
        <clipPath id="clipA"><rect width="750" height="250"/></clipPath>
      </defs>
      <g clip-path="url(#clipA)">
        <rect width="750" height="250" fill="var(--pattern)"/>
        <rect width="750" height="250" fill="var(--paper)" opacity="0.45"/>

        <g class="brand">
          <circle cx="30" cy="34" r="13" fill="var(--brand-blue)"/>
          <text class="brand-name" x="50" y="39">Kestrel Aid Services</text>
        </g>

        <path d="M0,178 C70,85 250,35 430,105 L430,250 L0,250 Z" fill="var(--brand-blue)"/>

        <circle cx="650" cy="215" r="252" fill="var(--brand-green)"/>
        <circle cx="658" cy="215" r="244" fill="url(#photoA)" role="img" aria-label="Photo of two smiling adults cheek to cheek outdoors"/>

        <circle cx="409" cy="45" r="35" fill="url(#orbA)"/>

        <text class="headline headline--light" x="228" y="99" text-anchor="middle">Support Coordination</text>
        <text class="headline headline--light" x="228" y="119" text-anchor="middle">Across New Jersey</text>

        <g class="features">
          <circle class="feature-badge" cx="89" cy="154" r="23"/>
          <text class="feature-text feature-text--light" x="122" y="148">Lorem ipsum</text>
          <text class="feature-text feature-text--light" x="122" y="163">dolor sit</text>

          <circle class="feature-badge" cx="258" cy="154" r="23"/>
          <text class="feature-text feature-text--light" x="292" y="148">Lorem ipsum</text>
          <text class="feature-text feature-text--light" x="292" y="163">dolor sit</text>

          <circle class="feature-badge" cx="89" cy="217" r="23"/>
          <text class="feature-text feature-text--light" x="122" y="211">Lorem ipsum</text>
          <text class="feature-text feature-text--light" x="122" y="226">dolor sit</text>

          <circle class="feature-badge" cx="258" cy="217" r="23"/>
          <text class="feature-text feature-text--light" x="292" y="211">Lorem ipsum</text>
          <text class="feature-text feature-text--light" x="292" y="226">dolor sit</text>
        </g>
      </g>
    </svg>
  </section>

  <!-- Banner variant B: curved band layout -->
  <section class="banner banner--curve" aria-label="Kestrel Aid Services banner, curved band layout">
    <svg viewBox="0 0 750 250">
      <defs>
        <linearGradient id="photoB" x1="0" y1="0" x2="1" y2="1">
          <stop offset="0" stop-color="var(--photo-green-a)"/>
          <stop offset="0.6" stop-color="var(--photo-green-b)"/>
          <stop offset="1" stop-color="#5f7c45"/>
        </linearGradient>
        <clipPath id="clipB"><rect width="750" height="250"/></clipPath>
      </defs>
      <g clip-path="url(#clipB)">
        <rect width="750" height="250" fill="var(--pattern)"/>
        <rect width="750" height="250" fill="var(--paper)" opacity="0.45"/>

        <path class="curve-band" d="M430,0 H480 C425,55 405,140 405,250 H355 C362,140 385,55 430,0 Z" fill="var(--brand-blue)"/>

        <path d="M480,0 H750 V250 H405 C405,140 425,55 480,0 Z" fill="url(#photoB)" stroke="var(--paper)" stroke-width="3" role="img" aria-label="Photo of a child and a woman playing with a toy airplane outdoors"/>

        <g class="brand">
          <circle cx="30" cy="34" r="13" fill="var(--brand-blue)"/>
          <text class="brand-name" x="50" y="39">Kestrel Aid Services</text>
        </g>

        <text class="headline headline--dark" x="37" y="99">Support Coordination</text>
        <text class="headline headline--dark" x="37" y="119">Across New Jersey</text>

        <g class="features">
          <circle class="feature-badge" cx="54" cy="154" r="23"/>
          <text class="feature-text feature-text--dark" x="88" y="148">Lorem ipsum</text>
          <text class="feature-text feature-text--dark" x="88" y="163">dolor sit</text>

          <circle class="feature-badge" cx="224" cy="154" r="23"/>
          <text class="feature-text feature-text--dark" x="258" y="148">Lorem ipsum</text>
          <text class="feature-text feature-text--dark" x="258" y="163">dolor sit</text>

          <circle class="feature-badge" cx="54" cy="217" r="23"/>
          <text class="feature-text feature-text--dark" x="88" y="211">Lorem ipsum</text>
          <text class="feature-text feature-text--dark" x="88" y="226">dolor sit</text>

          <circle class="feature-badge" cx="224" cy="217" r="23"/>
          <text class="feature-text feature-text--dark" x="258" y="211">Lorem ipsum</text>
          <text class="feature-text feature-text--dark" x="258" y="226">dolor sit</text>
        </g>
      </g>
    </svg>
  </section>
</main>
</body>
</html>
```